Plumbing Company After Business Card

Business card for a plumbing business that offers a variety of plumbing services including maintenance, domestic and commercial plumbing. My main focus is to offer high quality professional service. A logo on the card would be ideal. Any other questions feel free to email. Cheers

Looking for something modern and upmarket with preferably a matte black background

Business name is Keystone Plumbing and Gas

Industry/Entity Type

Plumbing

Contact Information for Business Card

Keystone Plumbing and Gas
Marcus Thornell
0427915368
14 Corrigan Road, Elmvale 3561
keystoneplumbing@mailbay.com.au
ABN 52 647 183 925

Font styles to use
Sans Serif

Colors
1b1b1b
ffffff
3377b5

Requirements
Must have
• Domestic
• Commercial
• Maintenance

```html
<!DOCTYPE html>
<html lang="en">
<head>
<meta charset="utf-8">
<title>Keystone Plumbing and Gas – Business Card</title>
<link href="https://fonts.googleapis.com/css2?family=Montserrat:wght@400;600;700;800&display=swap" rel="stylesheet">
<style>
  :root {
    --stage: #1b1b1b;
    --card-blue: #336f9e;
    --band-slate: #4a5b70;
    --paper: #ffffff;
    --ink-light: #ffffff;
    --accent-blue: #3377b5;
  }
  * { box-sizing: border-box; margin: 0; padding: 0; }
  html, body {
    width: 1200px; height: 1200px; overflow: hidden;
    background: var(--stage);
    font-family: "Montserrat", Arial, sans-serif;
  }
  .card {
    position: absolute; left: 150px; width: 871px; height: 510px;
    background: var(--card-blue); overflow: hidden;
    border: 1px solid #5a6470;
  }
  .card--front { top: 50px; }
  .card--back { top: 604px; }
  .top-band {
    position: absolute; left: 0; top: 0; width: 100%; height: 137px;
    background: var(--paper);
  }
  .top-band__pattern {
    position: absolute; top: 0; height: 100px;
    background: radial-gradient(ellipse at 40% 20%, rgba(156,200,234,.75), rgba(220,220,220,.5) 55%, rgba(255,255,255,0) 80%);
  }
  .card--front .top-band__pattern { left: 0; width: 625px; }
  .card--back .top-band__pattern { left: 255px; width: 616px; height: 130px; }
  .bottom-pattern {
    position: absolute; left: 15px; bottom: 0; width: 810px; height: 90px;
    background: radial-gradient(ellipse at 55% 110%, rgba(80,140,200,.55), rgba(120,150,185,.35) 55%, rgba(51,111,158,0) 80%);
  }
  .name-band {
    position: absolute; left: 37px; top: 262px; right: 0; height: 98px;
    background: var(--band-slate);
    border-top-left-radius: 48px;
    display: flex; align-items: center; gap: 66px; padding-left: 53px;
  }
  .name-band__dot {
    width: 24px; height: 24px; border-radius: 50%; background: var(--ink-light);
    flex: none;
  }
  .name-band__title {
    color: var(--ink-light); font-weight: 800; font-size: 36px;
    letter-spacing: .3px; white-space: nowrap;
  }
  .services {
    position: absolute; left: 180px; top: 382px;
    color: var(--ink-light); font-weight: 600; font-size: 18px;
    letter-spacing: 3px; white-space: nowrap;
  }
  .brand-mark {
    position: absolute; left: 62px; top: 58px;
    color: var(--accent-blue); font-weight: 700; font-size: 17px;
    letter-spacing: .5px; white-space: nowrap;
  }
  .contact-person {
    position: absolute; right: 56px; top: 178px; text-align: right;
    color: var(--ink-light); font-weight: 700; font-size: 25px; line-height: 33px;
    letter-spacing: .4px;
  }
  .company-details {
    position: absolute; left: 67px; top: 258px; color: var(--ink-light);
  }
  .company-details__name {
    font-weight: 800; font-size: 27px; letter-spacing: .3px; margin-bottom: 6px;
  }
  .company-details__line {
    font-weight: 400; font-size: 25px; line-height: 32px; letter-spacing: .5px;
  }
</style>
</head>
<body>
  <section class="card card--front">
    <div class="top-band">
      <div class="top-band__pattern" role="img" aria-label="Decorative pattern of overlapping blue and grey gears"></div>
    </div>
    <div class="name-band">
      <span class="name-band__dot"></span>
      <h1 class="name-band__title">KEYSTONE PLUMBING AND GAS</h1>
    </div>
    <p class="services">DOMESTIC • COMMERCIAL • MAINTENANCE</p>
    <div class="bottom-pattern" role="img" aria-label="Decorative row of faint gears along the bottom edge"></div>
  </section>

  <section class="card card--back">
    <div class="top-band">
      <div class="top-band__pattern" role="img" aria-label="Decorative gears with scattered blue and purple dots"></div>
      <div class="brand-mark">Keystone Plumbing and Gas</div>
    </div>
    <div class="contact-person">
      <p>Marcus Thornell</p>
      <p>0427915368</p>
    </div>
    <div class="company-details">
      <h2 class="company-details__name">KEYSTONE PLUMBING AND GAS</h2>
      <p class="company-details__line">14 Corrigan Road, Elmvale 3561</p>
      <p class="company-details__line">keystoneplumbing@mailbay.com.au</p>
      <p class="company-details__line">ABN 52 647 183 925</p>
    </div>
    <div class="bottom-pattern" role="img" aria-label="Decorative row of faint gears along the bottom edge"></div>
  </section>
</body>
</html>
```